We need a logo and landing page designed. We are a full-service general contractor based in Tempe Arizona. We can provide all phases of construction from design to completion. We specialize in commercial and residential remodels, as well as ground-up construction. We will like to see designs that primarily used reds, blues, blacks, whites, etc. The design should be a professional yet fun, easy-to-read format. Our name is Oak Harbor Construction...I would like to see some designs that incorporate a "oak harbor" and some without.
The final design should communicate a professional, quality-driven, safety oriented full service business.

Target Market(s)

Building owners, land developers, homeowners

Industry/Entity Type

Commercial Construction

Coding

Coded - Design and coding required

Number of Pages Required

1 page

Font styles to use
Serif

Colors
0054AA
0677BA
7BADD7
CADEEF
E8F1F8
59FF00
82FF00
B8FF75
E3FFCB
F4FFEA
EE7325
F08F49
F5BC92
FAE3D3
FDF4ED
EB3D1F
EC4F4E
F09395
F8D3D4
FCEDEE

```html
<!DOCTYPE html>
<html lang="en">
<head>
<meta charset="utf-8">
<title>Oak Harbor Construction</title>
<link href="https://fonts.googleapis.com/css2?family=Raleway:wght@500;600;700;800&family=Open+Sans:wght@400;600;700&display=swap" rel="stylesheet">
<style>
:root{
  --red:#e3262c;
  --red-dark:#c41d23;
  --ink:#1d1d1f;
  --dark:#232326;
  --card:#2f2f33;
  --text:#555;
  --muted:#8a8a8a;
  --light:#f2f2f2;
  --white:#fff;
  --line:#e2e2e2;
}
*{box-sizing:border-box;margin:0;padding:0}
html,body{width:1200px;height:4316px;overflow:hidden}
body{font-family:"Open Sans",Arial,sans-serif;color:var(--text);background:var(--white)}
h1,h2,h3,h4,.brand{font-family:"Raleway",Arial,sans-serif}
.btn{display:inline-block;background:var(--red);color:var(--white);font:700 13px "Open Sans",Arial,sans-serif;letter-spacing:.5px;text-transform:uppercase;padding:12px 24px;border-radius:3px;text-decoration:none}
.btn-sm{font-size:9px;padding:5px 10px;border-radius:2px}
.photo{display:block}

/* hero */
.hero{position:relative;height:660px;overflow:hidden}
.hero .photo{position:absolute;inset:0;background:linear-gradient(180deg,#0f2d5e 0%,#2a4f86 35%,#3e4b5c 60%,#2c3a22 85%,#1b2414 100%)}
.hero .shade{position:absolute;inset:0;background:rgba(10,15,30,.25)}
.topbar{position:absolute;top:0;left:0;right:0;height:130px;padding:0 100px;display:flex;flex-direction:column}
.topbar-row{display:flex;align-items:center;justify-content:space-between}
.topbar-row.upper{height:62px}
.brand{color:var(--white);font-weight:700;font-size:21px}
.top-contact{display:flex;align-items:center;gap:22px;color:var(--white);font-weight:700;font-size:17px}
.top-contact .phone{display:flex;align-items:center;gap:8px}
.nav{display:flex;justify-content:flex-end;gap:34px;list-style:none;margin-top:-6px}
.nav a{color:var(--white);font-size:13px;font-weight:600;text-decoration:none;text-transform:uppercase;padding:10px 14px;display:block}
.nav a.active{background:var(--red)}
.hero-copy{position:absolute;top:350px;left:0;right:0;text-align:center;color:var(--white)}
.hero-copy h1{font-size:58px;font-weight:800;letter-spacing:1px;text-transform:uppercase;text-shadow:0 2px 8px rgba(0,0,0,.4)}
.hero-copy p{font-size:24px;font-weight:700;margin-top:6px}
.hero-copy .actions{margin-top:30px;display:flex;justify-content:center;gap:18px}
.dots{position:absolute;bottom:36px;left:0;right:0;display:flex;justify-content:center;gap:8px}
.dots span{width:10px;height:10px;border-radius:50%;background:rgba(255,255,255,.5)}
.dots span.on{background:var(--white)}

/* about */
.about{height:512px;display:flex;padding:48px 132px 0;gap:36px}
.about .photo{width:488px;height:412px;background:linear-gradient(135deg,#e8e4de,#b7aca0 55%,#6a5a4c)}
.about-copy{padding-top:62px;width:400px}
.tag{display:inline-block;border:1px solid #d6d6d6;color:var(--ink);font-size:12px;font-weight:600;padding:6px 12px;box-shadow:-4px 0 0 var(--red)}
.about-copy h2{color:var(--ink);font-size:30px;font-weight:700;margin:20px 0 18px}
.about-copy p{font-size:13px;line-height:1.75;margin-bottom:26px}

/* services */
.services{height:488px;background:var(--dark);padding-top:40px}
.section-title{text-align:center;font-size:28px;font-weight:700}
.services .section-title{color:var(--white)}
.service-grid{display:grid;grid-template-columns:452px 452px;gap:30px 36px;justify-content:center;margin-top:34px}
.service{background:var(--card);display:flex;gap:18px;padding:22px 24px;height:160px}
.service svg{flex:none}
.service h3{color:var(--white);font-size:17px;font-weight:700;margin-bottom:8px}
.service p{color:#bdbdbd;font-size:11px;line-height:1.6;margin-bottom:10px}

/* difference */
.different{height:808px;position:relative;padding-top:60px;overflow:hidden}
.different .section-title{color:var(--ink)}
.different .section-title span{color:var(--red)}
.sketch-bg{position:absolute;left:560px;right:0;top:150px;height:600px;background:linear-gradient(160deg,#f7f7f7,#ececec)}
.diff-list{position:absolute;left:132px;top:180px;width:400px;list-style:none}
.diff-list li{display:flex;gap:18px;padding:16px 0;border-bottom:1px solid var(--line)}
.diff-list h4{color:var(--ink);font-size:15px;font-weight:700;margin-bottom:6px}
.diff-list p{font-size:11px;line-height:1.6}
.different .photo{position:absolute;left:600px;top:220px;width:472px;height:460px;background:linear-gradient(180deg,#c9d4dc 0%,#a68a6a 45%,#6a4e36 100%)}

/* build */
.build{height:492px;background:var(--light);position:relative;overflow:hidden}
.build .photo{position:absolute;left:132px;top:32px;width:488px;height:448px;background:linear-gradient(180deg,#d8dde0,#9aa6a5 50%,#3f4a45)}
.build-copy{position:absolute;left:660px;top:126px;width:440px}
.eyebrow{color:var(--ink);font-size:12px;font-weight:700;text-transform:uppercase;letter-spacing:.5px}
.build-copy h2{color:var(--ink);font-size:30px;font-weight:700;line-height:1.25;margin:10px 0 14px}
.build-copy p{font-size:12px;line-height:1.6;margin-bottom:20px}

/* testimonials */
.testimonials{height:590px;background:#2a2a2d;padding-top:64px;position:relative}
.testimonials .section-title{color:var(--white)}
.quotes{display:flex;justify-content:center;gap:36px;margin-top:52px}
.quote{width:290px;height:352px;background:rgba(60,60,64,.85);text-align:center;padding:28px 28px 0}
.quote .mark{color:var(--red);font:800 44px/1 "Raleway",Arial,sans-serif}
.quote p{color:#dcdcdc;font-size:13px;line-height:1.7;margin-top:10px}
.author{display:flex;align-items:center;justify-content:center;gap:10px;margin-top:20px;color:var(--white);font-size:13px;text-align:left}
.avatar{width:36px;height:36px;border-radius:50%;background:#8c8c90}
.arrow{position:absolute;top:294px}

/* cta */
.cta{height:370px;background:linear-gradient(180deg,#fafafa,#ececec);text-align:center;padding-top:82px}
.cta h2{color:#2d2d2d;font-family:"Open Sans",Arial,sans-serif;font-weight:400;font-size:32px;line-height:1.3}
.cta .btn{margin-top:28px}

/* footer */
.footer{height:368px;background:#121213;padding:72px 140px 0;display:flex}
.footer .brand{font-size:22px;width:308px;padding-top:100px}
.fcol{color:#cfcfcf;font-size:11px}
.fcol h4{color:var(--white);font-size:12px;font-weight:700;text-transform:uppercase;margin-bottom:14px;font-family:"Open Sans",Arial,sans-serif}
.fcol.menu{width:200px}
.fcol.menu ul{list-style:none;line-height:1.9;text-transform:uppercase}
.fcol.contact{width:312px}
.fcol.follow{width:140px}
.frow{display:flex;align-items:flex-start;gap:12px;margin-bottom:16px;line-height:1.5}
.ficon{width:28px;height:28px;border-radius:50%;background:var(--white);flex:none;display:flex;align-items:center;justify-content:center}
.copyright{height:28px;background:#121213;color:#9a9a9a;font-size:10px;text-align:center;line-height:28px}
</style>
</head>
<body>

<header class="hero">
  <div class="photo" role="img" aria-label="Two-storey house with porch lit at dusk among trees"></div>
  <div class="shade"></div>
  <div class="topbar">
    <div class="topbar-row upper">
      <span class="brand">Oak Harbor Construction</span>
      <div class="top-contact">
        <span class="phone">
          <svg width="18" height="18" viewBox="0 0 24 24"><path fill="#e3262c" d="M6.6 10.8a15 15 0 0 0 6.6 6.6l2.2-2.2a1 1 0 0 1 1-.25 11.4 11.4 0 0 0 3.6.6 1 1 0 0 1 1 1V20a1 1 0 0 1-1 1A17 17 0 0 1 3 4a1 1 0 0 1 1-1h3.5a1 1 0 0 1 1 1c0 1.25.2 2.45.57 3.57a1 1 0 0 1-.25 1z"/></svg>
          +1 888 888 8888
        </span>
        <a class="btn" href="#">Request Estimate</a>
      </div>
    </div>
    <ul class="nav">
      <li><a class="active" href="#">Home</a></li>
      <li><a href="#">About Us</a></li>
      <li><a href="#">Services</a></li>
      <li><a href="#">Projects</a></li>
      <li><a href="#">Testimonial</a></li>
      <li><a href="#">Contact Us</a></li>
    </ul>
  </div>
  <div class="hero-copy">
    <h1>Construction &amp; Remodel</h1>
    <p>Lorem Ipsum is simply dummy text of the printing and typesetting industry</p>
    <div class="actions"><a class="btn" href="#">Read More</a><a class="btn" href="#">Contact Us</a></div>
  </div>
  <div class="dots"><span class="on"></span><span></span><span></span></div>
</header>

<section class="about">
  <div class="photo" role="img" aria-label="Bright modern living room interior with sofa and large windows"></div>
  <div class="about-copy">
    <span class="tag">Welcome to our site</span>
    <h2>Imagine your perfect home</h2>
    <p>There are many variations of passages of Lorem Ipsum available, but the majority have suffered alteration in some form, by injected humour, or randomised words which don't look even slightly believable. If you are going to use a passage of Lorem Ipsum, you need to be sure there isn't anything embarrassing hidden in the middle of text. All the Lorem Ipsum generators on the Internet tend to repeat predefined.</p>
    <a class="btn" href="#">Read More</a>
  </div>
</section>

<section class="services">
  <h2 class="section-title">Our Services</h2>
  <div class="service-grid">
    <article class="service">
      <svg width="56" height="56" viewBox="0 0 56 56" fill="none" stroke="#fff" stroke-width="2"><path d="M6 28 28 8l22 20"/><path d="M12 23v26h32V23"/><rect x="23" y="34" width="10" height="15"/></svg>
      <div><h3>Residential Remodeling</h3><p>Lorem Ipsum is simply dummy text of the printing and typesetting industry. Lorem Ipsum has been the industry's standard dummy text ever since the 1500s.</p><a class="btn btn-sm" href="#">Read More</a></div>
    </article>
    <article class="service">
      <svg width="56" height="56" viewBox="0 0 56 56" fill="none" stroke="#fff" stroke-width="2"><rect x="10" y="10" width="20" height="40"/><rect x="30" y="22" width="16" height="28"/><path d="M15 17h10M15 25h10M15 33h10M35 29h6M35 37h6"/></svg>
      <div><h3>Commercial Remodeling</h3><p>Lorem Ipsum is simply dummy text of the printing and typesetting industry. Lorem Ipsum has been the industry's standard dummy text ever since the 1500s.</p><a class="btn btn-sm" href="#">Read More</a></div>
    </article>
    <article class="service">
      <svg width="56" height="56" viewBox="0 0 56 56" fill="none" stroke="#fff" stroke-width="2"><path d="M8 12h40M14 12v38M10 50h10M14 12l10 10M36 12v12"/><rect x="30" y="24" width="12" height="8"/><path d="M26 50V36h20v14"/></svg>
      <div><h3>New Construction</h3><p>Lorem Ipsum is simply dummy text of the printing and typesetting industry. Lorem Ipsum has been the industry's standard dummy text ever since the 1500s.</p><a class="btn btn-sm" href="#">Read More</a></div>
    </article>
    <article class="service">
      <svg width="56" height="56" viewBox="0 0 56 56" fill="none" stroke="#fff" stroke-width="2"><rect x="8" y="10" width="40" height="36"/><path d="M8 20h40M18 28h20M18 36h12"/><path d="M36 34l6 6"/></svg>
      <div><h3>Design-Build Service</h3><p>Lorem Ipsum is simply dummy text of the printing and typesetting industry. Lorem Ipsum has been the industry's standard dummy text ever since the 1500s.</p><a class="btn btn-sm" href="#">Read More</a></div>
    </article>
  </div>
</section>

<section class="different">
  <div class="sketch-bg" role="img" aria-label="Faint architectural line sketch of a building"></div>
  <h2 class="section-title">What Makes <span>Us Different</span></h2>
  <ul class="diff-list">
    <li><svg width="30" height="30" viewBox="0 0 30 30" fill="none" stroke="#e3262c" stroke-width="2"><circle cx="15" cy="15" r="12"/><path d="M15 8v14M11 11h6a2 2 0 0 1 0 4h-4a2 2 0 0 0 0 4h6"/></svg><div><h4>Hidden Costs</h4><p>Lorem Ipsum is simply dummy text of the printing and typesetting industry. Lorem Ipsum has been the industry's.</p></div></li>
    <li><svg width="30" height="30" viewBox="0 0 30 30" fill="none" stroke="#e3262c" stroke-width="2"><path d="M6 24 20 10M18 6l6 6-4 4-6-6zM6 24l-2 2"/></svg><div><h4>Superior Product</h4><p>Lorem Ipsum is simply dummy text of the printing and typesetting industry. Lorem Ipsum has been the industry's.</p></div></li>
    <li><svg width="30" height="30" viewBox="0 0 30 30" fill="none" stroke="#e3262c" stroke-width="2"><path d="M6 24C6 12 14 6 25 6c0 11-6 19-18 19M6 24l10-10"/></svg><div><h4>Eco Friendly</h4><p>Lorem Ipsum is simply dummy text of the printing and typesetting industry. Lorem Ipsum has been the industry's.</p></div></li>
    <li><svg width="30" height="30" viewBox="0 0 30 30" fill="none" stroke="#e3262c" stroke-width="2"><path d="M15 3 25 7v7c0 7-5 11-10 13C10 25 5 21 5 14V7z"/><path d="m10 15 4 4 6-7"/></svg><div><h4>Trusted Sources</h4><p>Lorem Ipsum is simply dummy text of the printing and typesetting industry. Lorem Ipsum has been the industry's.</p></div></li>
    <li><svg width="30" height="30" viewBox="0 0 30 30" fill="none" stroke="#e3262c" stroke-width="2"><circle cx="15" cy="10" r="5"/><path d="M5 27c0-6 4-10 10-10s10 4 10 10"/></svg><div><h4>Expert Team</h4><p>Lorem Ipsum is simply dummy text of the printing and typesetting industry. Lorem Ipsum has been the industry's.</p></div></li>
  </ul>
  <div class="photo" role="img" aria-label="Construction crew in hard hats and safety vests reviewing plans on a building site"></div>
</section>

<section class="build">
  <div class="photo" role="img" aria-label="Multi-level atrium interior with balconies and seating"></div>
  <div class="build-copy">
    <span class="eyebrow">Build Experience</span>
    <h2>Care and respect<br>throughout the process.</h2>
    <p>There are many variations of passages of Lorem Ipsum available, but the majority have suffered alteration in some form, by injected humour, or randomised words which don't look even slightly believable. If you are going to use a passage of Lorem Ipsum, you need to be sure there isn't anything embarrassing hidden in the middle of text. All the Lorem Ipsum generators on the Internet tend to repeat predefined.</p>
    <a class="btn" href="#">Our Process</a>
  </div>
</section>

<section class="testimonials">
  <h2 class="section-title">Testimonials</h2>
  <svg class="arrow" style="left:74px" width="16" height="24" viewBox="0 0 16 24"><path d="M12 3 4 12l8 9" fill="none" stroke="#fff" stroke-width="3"/></svg>
  <svg class="arrow" style="right:74px" width="16" height="24" viewBox="0 0 16 24"><path d="m4 3 8 9-8 9" fill="none" stroke="#fff" stroke-width="3"/></svg>
  <div class="quotes">
    <figure class="quote"><div class="mark">&ldquo;</div><p>There are many variations of passages of Lorem Ipsum available, but the majority have suffered alteration in some form, by injected humour, or randomised words which don't look even slightly believable. If you are going to use a passage of Lorem Ipsum, you need.</p><figcaption class="author"><span class="avatar"></span><span>Daniel<br>Moreno</span></figcaption></figure>
    <figure class="quote"><div class="mark">&ldquo;</div><p>There are many variations of passages of Lorem Ipsum available, but the majority have suffered alteration in some form, by injected humour, or randomised words which don't look even slightly believable. If you are going to use a passage of Lorem Ipsum, you need.</p><figcaption class="author"><span class="avatar"></span><span>Daniel<br>Moreno</span></figcaption></figure>
    <figure class="quote"><div class="mark">&ldquo;</div><p>There are many variations of passages of Lorem Ipsum available, but the majority have suffered alteration in some form, by injected humour, or randomised words which don't look even slightly believable. If you are going to use a passage of Lorem Ipsum, you need.</p><figcaption class="author"><span class="avatar"></span><span>Daniel<br>Moreno</span></figcaption></figure>
  </div>
</section>

<section class="cta" role="img" aria-label="Faint line sketch of a house behind the call to action">
  <h2>Lorem Ipsum is simply dummy text of<br>the printing and typesetting industry</h2>
  <a class="btn" href="#">Contact Us</a>
</section>

<footer>
  <div class="footer">
    <span class="brand">Oak Harbor Construction</span>
    <div class="fcol menu">
      <h4>Menu</h4>
      <ul><li>Home</li><li>About Us</li><li>Services</li><li>Projects</li><li>Testimonial</li><li>Contact Us</li></ul>
    </div>
    <div class="fcol contact">
      <h4>Contact Us</h4>
      <div class="frow"><span class="ficon"><svg width="12" height="14" viewBox="0 0 12 14"><path d="M6 0a5 5 0 0 0-5 5c0 4 5 9 5 9s5-5 5-9a5 5 0 0 0-5-5zm0 7a2 2 0 1 1 0-4 2 2 0 0 1 0 4z" fill="#121213"/></svg></span><span>2180 Harbor View Rd Suite 4<br>Tempe, AZ 85281</span></div>
      <div class="frow"><span class="ficon"><svg width="12" height="12" viewBox="0 0 24 24"><path fill="#121213" d="M6.6 10.8a15 15 0 0 0 6.6 6.6l2.2-2.2a1 1 0 0 1 1-.25 11.4 11.4 0 0 0 3.6.6 1 1 0 0 1 1 1V20a1 1 0 0 1-1 1A17 17 0 0 1 3 4a1 1 0 0 1 1-1h3.5a1 1 0 0 1 1 1c0 1.25.2 2.45.57 3.57a1 1 0 0 1-.25 1z"/></svg></span><span>Call us<br>+1 888 888 8888</span></div>
      <div class="frow"><span class="ficon"><svg width="12" height="10" viewBox="0 0 12 10"><rect x=".5" y=".5" width="11" height="9" fill="none" stroke="#121213"/><path d="m.5.5 5.5 5 5.5-5" fill="none" stroke="#121213"/></svg></span><span>E-mail us<br>info@oakharborconstruction.com</span></div>
    </div>
    <div class="fcol follow">
      <h4>Follow Us</h4>
      <div class="frow"><span class="ficon"></span><span>Like us on<br>SOCIAL PAGE</span></div>
      <div class="frow"><span class="ficon"></span><span>Follow us on<br>NEWS FEED</span></div>
      <div class="frow"><span class="ficon"></span><span>Follow us on<br>NETWORK</span></div>
    </div>
  </div>
  <div class="copyright">Copyright © 2024 All Rights Reserved</div>
</footer>

</body>
</html>
```